Simple Modern Label for a Coconut oil product

We need a label designed for Organic Coconut oil. We would like the label to convey the gourmet/high quality product. It should be modern and simple and look like an artisinal product. The label will need to contain all the basic label requirements - Independence list, place for nutrition facts, our company logo etc.
The label will ultimately be printed as oil proof, so it will have a glossy appearance.
I have includes some examples that I like and a file with the logo.

Product Container - Wide Mount Clear Glass Jar: 4.75 inches tall (base to the bottom of the lid) and 9.5 in circumference
Label: Can be 1 or 2 separate labels, round, square and rectangle are okay
No larger than 3 inches high and 9 inches long

Target Market(s)

Middle Age home chef

Industry/Entity Type

Product

Requirements
Must have
• - logo (Attached below, I have this in multiple formats, let me know if you need them)
• - 14 FL OZ (414mL)
• - ingredient: organic unrefined whole kernel virgin coconut oil,
• - Manufacturer: XXX Y St., anywhere, CA, 99999
• - Distributed by Meadowfern Naturals, P.O. Box 5521, Oakland, CA 94612 www.MeadowfernNaturals.example
• - Certified Organic by Company Name
• - Product of Sri Lanka
Nice to have
• - Nutrition Facts
Should not have
• Clutter

```html
<!DOCTYPE html>
<html lang="en">
<head>
<meta charset="utf-8">
<title>Meadowfern Naturals — Virgin Coconut Oil Labels</title>
<link href="https://fonts.googleapis.com/css2?family=Questrial&display=swap" rel="stylesheet">
<style>
  :root {
    --page: #f6f6f8;
    --cocoa: #4b3f3b;
    --navy: #0f2246;
    --gold: #f2c21a;
    --gold-deep: #d9a90f;
    --amber: #f6b40e;
    --ink: #1d1b1c;
    --white: #ffffff;
    --fine: #e9e3dc;
  }
  html, body {
    margin: 0;
    width: 1200px;
    height: 913px;
    overflow: hidden;
    background: var(--page);
    font-family: "Questrial", "Century Gothic", sans-serif;
  }
  .label-row {
    position: relative;
    width: 1200px;
    height: 913px;
  }
  .label {
    position: absolute;
    top: 336px;
    width: 140px;
    height: 420px;
  }
  .label--cocoa { left: 133px; }
  .label--navy  { left: 525px; }
  .label--amber { left: 926px; }
  .label text { font-family: "Questrial", "Century Gothic", sans-serif; }
</style>
</head>
<body>
<main class="label-row">

  <!-- Cocoa label -->
  <svg class="label label--cocoa" viewBox="0 0 140 420" aria-label="Virgin coconut oil label, cocoa brown">
    <path class="label-shape" d="M0 70 A70 70 0 0 1 140 70 V412 Q140 420 132 420 H8 Q0 420 0 412 Z" fill="var(--cocoa)"/>
    <path class="label-stitch" d="M4 70 A66 66 0 0 1 136 70 V410 Q136 416 130 416 H10 Q4 416 4 410 Z" fill="none" stroke="#ffffff" stroke-opacity=".45" stroke-width=".6" stroke-dasharray="2 1.5"/>
    <path class="label-stem" d="M48 122 C62 136 65 170 66 420 L74 420 C75 170 78 136 92 122 Z" fill="var(--gold)"/>
    <circle class="label-ring" cx="70" cy="69" r="57" fill="var(--cocoa)" stroke="var(--gold)" stroke-width="2"/>
    <rect class="brand-mark" x="22" y="62" width="11" height="11" fill="var(--white)"/>
    <text class="brand-name" x="37" y="71" font-size="8.4" fill="var(--white)">Meadowfern Naturals</text>
    <text class="product-name" transform="translate(58 352) rotate(-90)" font-size="18.5" fill="var(--white)">virgin coconut oil</text>
    <text class="net-volume" transform="translate(97 312) rotate(-90)" font-size="8" fill="var(--white)">14 FL OZ (414mL)</text>
    <g class="label-facts" font-size="4.4" fill="var(--fine)">
      <text transform="translate(106 404) rotate(-90)" textLength="250" lengthAdjust="spacingAndGlyphs">Ingredient: organic unrefined whole kernel virgin coconut oil · Product of Sri Lanka</text>
      <text transform="translate(113 404) rotate(-90)" textLength="250" lengthAdjust="spacingAndGlyphs">Manufacturer: XXX Y St., anywhere, CA, 99999 · Certified Organic by Company Name</text>
      <text transform="translate(120 404) rotate(-90)" textLength="250" lengthAdjust="spacingAndGlyphs">Distributed by Meadowfern Naturals, P.O. Box 5521, Oakland, CA 94612</text>
      <text transform="translate(127 404) rotate(-90)" textLength="140" lengthAdjust="spacingAndGlyphs">www.MeadowfernNaturals.example</text>
    </g>
  </svg>

  <!-- Navy label -->
  <svg class="label label--navy" viewBox="0 0 140 420" aria-label="Virgin coconut oil label, navy">
    <defs>
      <linearGradient id="goldSplit" x1="0" x2="1">
        <stop offset="0.5" stop-color="var(--gold)"/>
        <stop offset="0.5" stop-color="var(--gold-deep)"/>
      </linearGradient>
    </defs>
    <path class="label-shape" d="M0 70 A70 70 0 0 1 140 70 V412 Q140 420 132 420 H8 Q0 420 0 412 Z" fill="var(--navy)"/>
    <path class="label-stitch" d="M4 70 A66 66 0 0 1 136 70 V410 Q136 416 130 416 H10 Q4 416 4 410 Z" fill="none" stroke="#ffffff" stroke-opacity=".45" stroke-width=".6" stroke-dasharray="2 1.5"/>
    <path class="label-stem" d="M48 122 C62 136 65 170 66 420 L74 420 C75 170 78 136 92 122 Z" fill="url(#goldSplit)"/>
    <circle class="label-disc" cx="70" cy="69" r="58" fill="url(#goldSplit)"/>
    <rect class="brand-mark" x="22" y="62" width="11" height="11" fill="var(--white)"/>
    <text class="brand-name" x="37" y="71" font-size="8.4" fill="var(--white)">Meadowfern Naturals</text>
    <text class="product-name" transform="translate(58 352) rotate(-90)" font-size="18.5" fill="var(--white)">virgin coconut oil</text>
    <text class="net-volume" transform="translate(97 312) rotate(-90)" font-size="8" fill="var(--white)">14 FL OZ (414mL)</text>
    <g class="label-facts" font-size="4.4" fill="var(--fine)">
      <text transform="translate(106 404) rotate(-90)" textLength="250" lengthAdjust="spacingAndGlyphs">Ingredient: organic unrefined whole kernel virgin coconut oil · Product of Sri Lanka</text>
      <text transform="translate(113 404) rotate(-90)" textLength="250" lengthAdjust="spacingAndGlyphs">Manufacturer: XXX Y St., anywhere, CA, 99999 · Certified Organic by Company Name</text>
      <text transform="translate(120 404) rotate(-90)" textLength="250" lengthAdjust="spacingAndGlyphs">Distributed by Meadowfern Naturals, P.O. Box 5521, Oakland, CA 94612</text>
      <text transform="translate(127 404) rotate(-90)" textLength="140" lengthAdjust="spacingAndGlyphs">www.MeadowfernNaturals.example</text>
    </g>
  </svg>

  <!-- Amber label -->
  <svg class="label label--amber" viewBox="0 0 140 420" aria-label="Organic virgin coconut oil label, amber and black">
    <path class="label-shape" d="M0 70 A70 70 0 0 1 140 70 V412 Q140 420 132 420 H8 Q0 420 0 412 Z" fill="var(--amber)"/>
    <path class="label-black" d="M0 89 H22 C44 89 60 100 64 124 L66 146 H74 L76 124 C80 100 96 89 118 89 H140 V412 Q140 420 132 420 H8 Q0 420 0 412 Z" fill="var(--ink)"/>
    <path class="oil-drop" d="M70 138 C74 150 82 158 82 166 A12 12 0 0 1 58 166 C58 158 66 150 70 138 Z" fill="var(--amber)"/>
    <path class="oil-drop-shine" d="M62 166 A8 8 0 0 0 74 172" fill="none" stroke="#fff3c4" stroke-width="1.4"/>
    <rect class="brand-mark" x="22" y="47" width="11" height="11" fill="var(--ink)"/>
    <text class="brand-name" x="37" y="56" font-size="8.4" fill="var(--ink)">Meadowfern Naturals</text>
    <text class="product-kicker" x="70" y="210" font-size="12" text-anchor="middle" fill="var(--white)">Organic Virgin</text>
    <text class="product-name" x="70" y="240" font-size="28" text-anchor="middle" fill="var(--white)">coconut</text>
    <text class="product-type" x="71" y="263" font-size="16" text-anchor="middle" letter-spacing="9" fill="var(--white)">OIL</text>
    <rect class="coconut-illustration" x="0" y="284" width="140" height="64" fill="var(--amber)" role="img" aria-label="Line drawing of a whole coconut and a halved coconut with leaves"/>
    <g class="label-facts" font-size="4.4" fill="var(--fine)" text-anchor="middle">
      <text x="70" y="358">Ingredient: organic unrefined whole kernel</text>
      <text x="70" y="363.5">virgin coconut oil · Product of Sri Lanka</text>
      <text x="70" y="369">Manufacturer: XXX Y St., anywhere, CA, 99999</text>
      <text x="70" y="374.5">Distributed by Meadowfern Naturals</text>
      <text x="70" y="380">P.O. Box 5521, Oakland, CA 94612</text>
      <text x="70" y="385.5">www.MeadowfernNaturals.example</text>
      <text x="70" y="391">Certified Organic by Company Name</text>
    </g>
    <text class="net-volume" x="70" y="406" font-size="9.5" text-anchor="middle" fill="var(--white)">14 FL OZ (414mL)</text>
  </svg>

</main>
</body>
</html>
```